Clean business card with logo provided

I want a card that will stand out among the masses. I need the color and image to show professionalism and yet have a family appeal showing that I only deal with win/win scenarios. The back of the card will be used to take notes about the individual so I can use that in my database entry. I like modern design but need professionalism in it also. It needs to fit my "clean, safe, and affordable housing" motto. I need to be able to write on the file and update the card details for my employees.

Target Market(s)

Investors looking to make investment income through real estate

Industry/Entity Type

Real Estate

Contact Information for Business Card

Mark Dunthorpe
blank address, city, st, zip code
480-555-3174
markdunthorpe@brivoholdings.example
www.brivoholdings.example

Font styles to use
Sans Serif

Requirements
Must have
• I would like the back of the card to have lines for info. example
• Met/Visited: Date:
• Interets:
Nice to have
• I want the cards color to match the logo background color. Font with details to be san serif and black. I want the card rectangular with square corners. Standard business card size. I would like to see cards designed with both images to see which i prefer more.

```html
<!DOCTYPE html>
<html lang="en">
<head>
<meta charset="utf-8">
<title>Brivo Holdings LLC – Business Cards</title>
<link rel="stylesheet" href="https://fonts.googleapis.com/css2?family=Open+Sans:wght@400;600;700&display=swap">
<style>
  :root {
    --backdrop: #2a2a2c;
    --card: #ffffff;
    --teal: #29b1c6;
    --ink: #111111;
    --rule: #222222;
    --soft-rule: #e4e4e4;
  }
  * { box-sizing: border-box; margin: 0; padding: 0; }
  html, body { width: 1200px; height: 900px; overflow: hidden; }
  body {
    background: var(--backdrop);
    font-family: "Open Sans", Arial, sans-serif;
    color: var(--ink);
    position: relative;
  }
  .card {
    position: absolute;
    width: 560px;
    height: 320px;
    background: var(--card);
    border-radius: 26px;
    box-shadow: 0 18px 40px rgba(0,0,0,.45);
    overflow: hidden;
  }
  .card--notes { left: 60px; top: 110px; }
  .card--contact { left: 580px; top: 470px; }

  .brand { position: absolute; }
  .brand__name {
    display: flex; align-items: center; gap: 10px;
    font-size: 28px; font-weight: 600; color: var(--teal);
    letter-spacing: 1px; white-space: nowrap;
  }
  .brand__dot {
    width: 13px; height: 13px; border-radius: 50%; background: var(--teal);
  }
  .brand__tagline {
    font-size: 11.5px; font-weight: 600; color: var(--teal);
    margin-top: 4px; padding-left: 23px;
  }
  .card--notes .brand { left: 150px; top: 30px; }
  .card--contact .brand { left: 40px; top: 56px; }

  .blank-line {
    position: absolute; height: 0;
    border-top: 1.5px dashed #444;
  }
  .notes__heading {
    position: absolute; left: 44px; top: 178px;
    font-size: 17px; font-weight: 600; color: var(--teal);
  }
  .notes__field {
    position: absolute; left: 62px;
    display: flex; align-items: flex-end; gap: 4px;
    font-size: 14px; width: 460px;
  }
  .notes__field .blank-line { position: static; flex: 1; margin-bottom: 4px; }

  .contact__divider {
    position: absolute; left: 0; right: 0; top: 134px;
    border-top: 1px solid var(--soft-rule);
  }
  .contact__rule {
    position: absolute; left: 40px; right: 30px; top: 186px;
    border-top: 2px solid var(--rule);
  }
  .contact__name {
    position: absolute; left: 40px; top: 156px;
    font-size: 21px; font-weight: 700; letter-spacing: .5px;
  }
  .contact__address {
    position: absolute; right: 32px; top: 196px;
    text-align: right; font-size: 13.5px; line-height: 1.35;
    font-style: normal;
  }
  .contact__list {
    position: absolute; left: 40px; top: 232px;
    list-style: none; font-size: 13.5px; line-height: 1.55;
  }
  .contact__list li { display: flex; align-items: center; gap: 8px; }
  .contact__list svg { width: 11px; height: 11px; flex: none; }
</style>
</head>
<body>

<section class="card card--notes" aria-label="Notes side of card">
  <div class="brand">
    <div class="brand__name"><span class="brand__dot"></span>BRIVO HOLDINGS LLC</div>
    <div class="brand__tagline">Providing clean, safe, and affordable housing</div>
  </div>
  <div class="blank-line" style="left:260px; right:40px; top:120px;"></div>
  <div class="blank-line" style="left:160px; right:40px; top:150px;"></div>
  <p class="notes__heading">Met/Visited:</p>
  <div class="notes__field" style="top:200px;"><span>Name:</span><span class="blank-line"></span></div>
  <div class="notes__field" style="top:236px;"><span>Date:</span><span class="blank-line"></span></div>
  <div class="notes__field" style="top:272px;"><span>Interets:</span><span class="blank-line"></span></div>
</section>

<section class="card card--contact" aria-label="Contact side of card">
  <div class="brand">
    <div class="brand__name"><span class="brand__dot"></span>BRIVO HOLDINGS LLC</div>
    <div class="brand__tagline">Providing clean, safe, and affordable housing</div>
  </div>
  <div class="contact__divider"></div>
  <h1 class="contact__name">MARK DUNTHORPE</h1>
  <div class="contact__rule"></div>
  <address class="contact__address">
    2750 Harbor Lane<br>Maple Ridge, OH 44300
  </address>
  <ul class="contact__list">
    <li><svg viewBox="0 0 12 12"><path d="M2.5 1h2l1 2.5-1.3 1a6 6 0 0 0 3.3 3.3l1-1.3L11 7.5v2a1.2 1.2 0 0 1-1.3 1.2A9 9 0 0 1 1.3 2.3 1.2 1.2 0 0 1 2.5 1z" fill="var(--teal)"/></svg>480-555-3174</li>
    <li><svg viewBox="0 0 12 12"><rect x="1" y="2.5" width="10" height="7" fill="none" stroke="var(--teal)" stroke-width="1.2"/><path d="M1 2.5l5 4 5-4" fill="none" stroke="var(--teal)" stroke-width="1.2"/></svg>markdunthorpe@brivoholdings.example</li>
    <li><svg viewBox="0 0 12 12"><circle cx="6" cy="6" r="5" fill="none" stroke="var(--teal)" stroke-width="1.2"/><path d="M1 6h10M6 1c-2 2.5-2 7.5 0 10M6 1c2 2.5 2 7.5 0 10" fill="none" stroke="var(--teal)" stroke-width="1"/></svg>www.brivoholdings.example</li>
  </ul>
</section>

</body>
</html>
```